Cedar Row Maintenance and Concierge Flyer

We need a flyer for cedar row maintenance and concierge service. We specialize in and provide residential maintenance and errand services to retired and semi retired persons living in the Lake Norman area. The services we include:
Lighting and plumbing repairs
Ceiling fan installation
Handicap accessories
Locks and security
Picture hanging
Hang blinds
Furniture arrangement / assembly
Pressure washing
Battery Jump start
and more...

Our Concierge services include:
Errand running
Grocery shopping
Wellness Checks
Dog Walk
Garbage Collection
and more...

We offer monthly service agreements and 24/7 access
Call text or e-mail for more information
704.555.0187
1cedarrowmaint@quillpostmail.com

The design should invoke a sense of trust and a customer service driven mission

Target Market(s)

Residential maintenance

Industry/Entity Type

Property Maintenance

Contact Information for Business Card

Derek Halvorsen
48176 Quimby Ferrel Rd.
Cornelius NC 28031
704.555.0187
with uploaded logo

Requirements
Nice to have
• Would like a postcard size flyer. Front and back
Should not have
• No pics of of people wearing hard hats or pics of blueprints. No pics of commercial or industrial maintenance.

```html
<!DOCTYPE html>
<html lang="en">
<head>
<meta charset="utf-8">
<title>Cedar Row Maintenance and Concierge – Postcard Front and Back</title>
<link rel="stylesheet" href="https://fonts.googleapis.com/css2?family=Roboto:wght@400;500;700;900&family=Roboto+Condensed:wght@700&family=Lato:ital,wght@1,700&family=Kalam:wght@700&display=swap">
<style>
  :root {
    --red: #e31b23;
    --red-deep: #b3121a;
    --charcoal: #3d3d3f;
    --gray: #6b6b6e;
    --gray-light: #c9c9cb;
    --paper: #f4f4f4;
    --white: #ffffff;
    --ink: #111111;
    --backdrop: #e6e2dd;
  }
  * { margin: 0; padding: 0; box-sizing: border-box; }
  html, body { width: 900px; height: 1200px; overflow: hidden; }
  body { background: var(--backdrop); font-family: "Roboto", Arial, sans-serif; position: relative; }

  .postcard {
    position: absolute; left: 98px; width: 702px; height: 454px;
    overflow: hidden; background: var(--white);
    box-shadow: 0 6px 16px rgba(0,0,0,.25);
  }
  .postcard--front { top: 88px; }
  .postcard--back { top: 660px; }
  .postcard svg.card-art { position: absolute; inset: 0; }
  .abs { position: absolute; }

  .brand { display: flex; align-items: center; gap: 10px; }
  .brand__dot { width: 34px; height: 34px; border-radius: 50%; background: var(--red); flex: none; }
  .brand__name { font-weight: 500; font-size: 19px; color: var(--charcoal); line-height: 1.15; }

  .intro { left: 28px; top: 148px; width: 375px; color: var(--white); font-weight: 700; font-size: 13.5px; line-height: 19.5px; white-space: nowrap; }

  .tab { background: var(--charcoal); color: var(--white); font-weight: 700; text-align: center;
         clip-path: polygon(0 0, 100% 0, 93% 100%, 7% 100%); }
  .tab--services { left: 92px; top: 236px; width: 122px; height: 31px; font-size: 18px; line-height: 30px; }

  .service-list { list-style: none; font-family: "Lato", Arial, sans-serif; font-style: italic; font-weight: 700;
                  color: var(--white); font-size: 13px; line-height: 15.5px; }
  .service-list li { position: relative; padding-left: 14px; margin-bottom: 5px; }
  .service-list li::before { content: ""; position: absolute; left: 0; top: 6px; width: 5px; height: 5px; border-radius: 50%; background: var(--ink); }
  .service-list li.plain::before { display: none; }
  .col-divider { width: 1px; background: rgba(255,255,255,.35); }

  .pill { background: var(--charcoal); color: var(--white); border-radius: 12px; text-align: center;
          font-weight: 700; box-shadow: 0 1px 3px rgba(0,0,0,.4); }
  .pill--concierge { left: 25px; top: 45px; width: 196px; height: 22px; font-size: 12.5px; line-height: 22px; }

  .banner { left: 360px; top: 124px; width: 342px; height: 68px; background: var(--red); color: var(--white); text-align: center; }
  .banner__script { font-family: "Kalam", cursive; font-size: 21px; line-height: 24px; padding-top: 6px; letter-spacing: .3px; }
  .banner__bold { font-family: "Roboto Condensed", Arial, sans-serif; font-weight: 700; font-size: 27px; line-height: 30px; }

  .tab--offer { left: 466px; top: 212px; width: 112px; height: 30px; font-family: "Roboto Condensed", Arial, sans-serif; font-size: 21px; line-height: 30px; }
  .offer-red { left: 428px; top: 244px; width: 256px; text-align: center; color: var(--red);
               font-family: "Roboto Condensed", Arial, sans-serif; font-weight: 700; font-size: 35px; line-height: 38px; }
  .offer-gray { left: 428px; top: 280px; width: 256px; text-align: center; color: var(--charcoal);
                font-weight: 900; font-size: 37px; line-height: 40px; }

  .access-badge { left: 304px; top: 202px; width: 116px; height: 116px; border-radius: 50%;
                  background: var(--red); border: 4px solid var(--ink); color: var(--white); text-align: center;
                  font-family: "Roboto Condensed", Arial, sans-serif; font-weight: 700;
                  display: flex; flex-direction: column; justify-content: center; box-shadow: 0 2px 6px rgba(0,0,0,.35); }
  .access-badge__big { font-size: 36px; line-height: 34px; }
  .access-badge__small { font-size: 25px; line-height: 26px; }

  .pill--info { left: 424px; top: 330px; width: 212px; height: 50px; border-radius: 10px; background: var(--gray);
                font-size: 16.5px; line-height: 19px; padding-top: 6px; font-weight: 500; }

  .phone { left: 424px; top: 385px; width: 220px; color: var(--red); font-weight: 700; font-size: 24px;
           display: flex; align-items: center; gap: 6px; }
  .email { left: 424px; top: 418px; width: 270px; color: var(--white); font-size: 12.5px; display: flex; align-items: center; gap: 6px; }
</style>
</head>
<body>

<section class="postcard postcard--front">
  <svg class="card-art" width="702" height="454" viewBox="0 0 702 454">
    <defs>
      <linearGradient id="paperFront" x1="0" y1="0" x2="0" y2="1">
        <stop offset="0" stop-color="#ffffff"/><stop offset="1" stop-color="#e9e9ea"/>
      </linearGradient>
      <linearGradient id="bandGray" x1="0" y1="0" x2="1" y2="0">
        <stop offset="0" stop-color="#5a5a5c"/><stop offset=".7" stop-color="#8a8a8c"/><stop offset="1" stop-color="#d6d6d8"/>
      </linearGradient>
      <radialGradient id="redField" cx=".4" cy=".6" r=".8">
        <stop offset="0" stop-color="#ee2a31"/><stop offset="1" stop-color="#b3121a"/>
      </radialGradient>
      <linearGradient id="photoWorker" x1="0" y1="0" x2="0" y2="1">
        <stop offset="0" stop-color="#dfe5ea"/><stop offset=".55" stop-color="#b6c2cf"/><stop offset="1" stop-color="#3e4f6e"/>
      </linearGradient>
    </defs>
    <rect width="702" height="454" fill="url(#paperFront)"/>
    <rect x="0" y="118" width="440" height="6" fill="var(--red)"/>
    <rect x="0" y="140" width="450" height="72" fill="url(#bandGray)"/>
    <path d="M0,232 L190,232 C340,232 470,300 560,380 C615,425 660,418 702,402 L702,454 L0,454 Z" fill="url(#redField)"/>
    <path d="M200,230 C350,232 480,298 565,376 C618,422 665,412 702,396" fill="none" stroke="#8d8d90" stroke-width="5"/>
    <circle cx="567" cy="212" r="156" fill="#ffffff"/>
    <path d="M430,110 A156,156 0 0 1 640,62" fill="none" stroke="var(--red)" stroke-width="9"/>
    <circle cx="567" cy="212" r="148" fill="url(#photoWorker)" stroke="#9a9a9d" stroke-width="3" role="img" aria-label="Photo of a smiling handyman in a plaid shirt giving an OK sign"/>
  </svg>

  <div class="brand abs" style="left:92px; top:38px;">
    <span class="brand__dot"></span>
    <span class="brand__name">Cedar Row<br>Maintenance &amp; Concierge</span>
  </div>

  <p class="intro abs">We specialize in and provide residential maintenance<br>and errand services to retired and semi retired persons<br>living in the Lake Norman area.</p>

  <div class="tab tab--services abs">services</div>

  <ul class="service-list abs" style="left:22px; top:297px; width:165px;">
    <li>Lighting and plumbing repairs</li>
    <li>Ceiling fan installation</li>
    <li>Handicap accessories</li>
    <li>Locks and security</li>
    <li>Picture hanging</li>
  </ul>
  <div class="col-divider abs" style="left:192px; top:296px; height:112px;"></div>
  <ul class="service-list abs" style="left:220px; top:297px; width:160px;">
    <li>Hang blinds</li>
    <li>Furniture arrangement / assembly</li>
    <li>Pressure washing</li>
    <li>Battery Jump start</li>
    <li>and more...</li>
  </ul>
</section>

<section class="postcard postcard--back">
  <svg class="card-art" width="702" height="454" viewBox="0 0 702 454">
    <defs>
      <linearGradient id="paperBack" x1="0" y1="0" x2="0" y2="1">
        <stop offset="0" stop-color="#ffffff"/><stop offset="1" stop-color="#e4e4e5"/>
      </linearGradient>
      <linearGradient id="redCircle" x1="0" y1="0" x2="0" y2="1">
        <stop offset="0" stop-color="#e31b23"/><stop offset=".45" stop-color="#e8323a"/><stop offset="1" stop-color="#c21820"/>
      </linearGradient>
      <linearGradient id="photoCouple" x1="0" y1="0" x2="1" y2="1">
        <stop offset="0" stop-color="#f2a393"/><stop offset=".5" stop-color="#e2705f"/><stop offset="1" stop-color="#b33a2e"/>
      </linearGradient>
      <clipPath id="circleClip"><circle cx="160" cy="222" r="220"/></clipPath>
    </defs>
    <rect width="702" height="454" fill="url(#paperBack)"/>
    <path d="M300,454 C380,380 520,362 702,372 L702,454 Z" fill="var(--ink)"/>
    <path d="M300,454 C380,380 520,362 702,372" fill="none" stroke="#9a9a9d" stroke-width="4"/>
    <circle cx="160" cy="222" r="238" fill="#8f8f92"/>
    <circle cx="160" cy="222" r="229" fill="#ffffff"/>
    <circle cx="160" cy="222" r="220" fill="url(#redCircle)"/>
    <rect x="0" y="165" width="400" height="300" fill="url(#photoCouple)" clip-path="url(#circleClip)" role="img" aria-label="Red-tinted photo of a smiling senior couple seated together"/>
  </svg>

  <div class="pill pill--concierge abs">Our Concierge services include:</div>
  <ul class="service-list abs" style="left:22px; top:92px; width:140px;">
    <li>Errand running</li>
    <li>Grocery shopping</li>
    <li>Wellness Checks</li>
  </ul>
  <div class="col-divider abs" style="left:157px; top:92px; height:60px;"></div>
  <ul class="service-list abs" style="left:166px; top:92px; width:140px;">
    <li>Dog Walk</li>
    <li>Garbage Collection</li>
    <li class="plain">and more...</li>
  </ul>

  <div class="brand abs" style="left:372px; top:34px;">
    <span class="brand__dot"></span>
    <span class="brand__name">Cedar Row<br>Maintenance &amp; Concierge</span>
  </div>

  <div class="banner abs">
    <div class="banner__script">cedar row maintenance</div>
    <div class="banner__bold">and concierge service</div>
  </div>

  <div class="tab tab--offer abs">We offer</div>
  <div class="offer-red abs">monthly service</div>
  <div class="offer-gray abs">agreements</div>

  <div class="access-badge abs">
    <span class="access-badge__big">24/7</span>
    <span class="access-badge__small">access</span>
  </div>

  <div class="pill pill--info abs">Call text or e-mail for<br>more information</div>

  <div class="phone abs">
    <svg width="16" height="18" viewBox="0 0 16 18" aria-hidden="true"><rect x="1" y="1" width="14" height="16" rx="3" fill="var(--red)"/><path d="M5,4 C4,7 6,12 10,14 L11.5,12.5 L9.5,10.8 L8.6,11.6 C7.4,10.6 6.6,9.2 6.4,7.8 L7.4,7.1 L6.6,4.6 Z" fill="var(--ink)"/></svg>
    <span>704-555-0187</span>
  </div>
  <div class="email abs">
    <svg width="14" height="10" viewBox="0 0 14 10" aria-hidden="true"><rect width="14" height="10" fill="#ffffff"/><path d="M0,0 L7,6 L14,0" fill="none" stroke="#111" stroke-width="1.2"/></svg>
    <span>1cedarrowmaint@quillpostmail.com</span>
  </div>
</section>

</body>
</html>
```